Fernhollow Lodges Website

We need a revamp on our website. We would like to keep the same "vibe", the Brindlemoor style, and all the content. But we need a more appealing website, with new pictures of everything.

Preferably done by Pagecraft or Zolo.

www.fernhollowlodges-example.com

```html
<!DOCTYPE html>
<html lang="en">
<head>
<meta charset="utf-8">
<title>Fernhollow Lodges</title>
<link href="https://fonts.googleapis.com/css2?family=Luckiest+Guy&family=Oswald:wght@400;500&family=Lato:wght@400;700&display=swap" rel="stylesheet">
<style>
:root{
  --wood-a:#6f7f96;
  --wood-b:#8a7260;
  --sky:#1d4f9c;
  --cream:#efe5d1;
  --cream-dark:#e7dcc6;
  --ink:#2a2420;
  --text:#3c3530;
  --brown:#7b4a1f;
  --footer:#221a14;
  --white:#ffffff;
  --rule:#b8864f;
}
*{box-sizing:border-box;margin:0;padding:0}
html,body{width:1200px;height:3364px;overflow:hidden}
body{position:relative;font-family:'Lato',sans-serif;color:var(--text);
  background:linear-gradient(90deg,var(--wood-a),var(--wood-b) 30%,var(--wood-a) 55%,var(--wood-b) 80%,var(--wood-a))}
.display{font-family:'Luckiest Guy','Arial Black',sans-serif;white-space:nowrap}
.backdrop{position:absolute;left:0;top:0;width:1200px;height:430px;
  background:linear-gradient(180deg,#0f3a85 0%,var(--sky) 40%,#3a5e7a 75%,rgba(111,127,150,0) 100%)}
.page{position:absolute;left:117px;top:0;width:966px}
.brand{height:161px;display:flex;align-items:center;justify-content:center;gap:14px}
.brand-mark{width:34px;height:34px;background:var(--brown);border-radius:50%}
.brand-name{font-size:36px;color:#2a1b10;letter-spacing:1px}
.nav{height:52px;background:#17120e;display:flex;align-items:center;padding:0 22px;white-space:nowrap;
  font-family:'Oswald','Arial Narrow',sans-serif;font-size:12.5px;color:var(--white);text-transform:uppercase}
.nav a{color:inherit;text-decoration:none;margin-right:22px;white-space:nowrap}
.nav .phone{margin-left:auto;margin-right:0;font-size:18px;text-transform:none}
.main{background:var(--cream);padding-top:18px}
.hero{position:relative;margin:0 15px;height:505px;
  background:linear-gradient(180deg,#3a4634 0%,#2d2a22 45%,#473827 70%,#2b3322 100%);
  display:flex;flex-direction:column;align-items:center;justify-content:center}
.hero-title{font-size:50px;line-height:58px;color:var(--white);text-align:center;letter-spacing:2px;margin-top:-40px;font-weight:400}
.btn{display:inline-block;background:var(--brown);color:var(--white);
  font-size:15px;letter-spacing:1px;border-radius:22px;text-transform:uppercase}
.hero .btn{margin-top:22px;padding:12px 26px 9px}
.arrow{position:absolute;top:50%;margin-top:-10px}
.arrow.left{left:14px}.arrow.right{right:14px}
.welcome{text-align:center;padding:65px 92px 0;height:657px}
.h2{color:var(--ink);font-size:36px;letter-spacing:2px;text-transform:uppercase;font-weight:400}
.welcome p{font-size:13.5px;line-height:27.5px;margin-top:22px}
.h4{font-size:17px;letter-spacing:1px;color:var(--ink);text-transform:uppercase;margin-top:36px;font-weight:400}
.amenities{display:flex;justify-content:space-between;margin:28px -48px 0}
.amenity{width:140px;text-align:center;font-size:14px;line-height:24px}
.amenity svg{display:block;margin:0 auto 12px;height:56px}
.newsletter{height:386px;background:linear-gradient(180deg,#161b22 0%,#24231f 45%,#3b3026 75%,#2b2722 100%);
  text-align:center;color:var(--white);padding-top:90px}
.newsletter .h2{color:var(--white)}
.newsletter p{font-size:15px;line-height:28px;margin-top:12px}
.signup{display:flex;justify-content:center;gap:8px;margin-top:20px;margin-left:-4px}
.field{width:458px;height:42px;border-radius:21px;background:var(--white);color:#777;font-size:12px;text-align:left;padding:14px 18px}
.signup .btn{padding:14px 20px 11px;font-size:14px}
.features{display:flex;gap:42px;padding:69px 33px 0;height:673px;border-bottom:2px solid var(--rule)}
.feature{width:429px}
.h3{font-size:22px;letter-spacing:1px;color:var(--ink);text-transform:uppercase;font-weight:400}
.photo{margin-top:25px;height:245px;border:5px solid var(--white);box-shadow:0 1px 4px rgba(0,0,0,.25)}
.photo.lodge{background:linear-gradient(180deg,#3c4a3a,#27301f 50%,#5a4a36)}
.photo.cottage{background:linear-gradient(180deg,#4a5a44,#473a2c 50%,#384230)}
.feature p{font-size:13.5px;line-height:27px;margin-top:28px}
.outline-btn{display:inline-flex;align-items:center;gap:6px;margin-top:28px;border:2px solid var(--ink);padding:9px 16px 6px;
  font-size:14px;letter-spacing:1px;color:var(--ink);box-shadow:2px 2px 0 rgba(0,0,0,.35);text-transform:uppercase}
.reviews{height:421px;background:var(--cream-dark);text-align:center;padding:75px 80px 0}
.reviewer{display:flex;justify-content:center;align-items:center;gap:10px;margin-top:16px;
  font-size:15px;color:var(--ink);letter-spacing:1px;text-transform:uppercase}
.quote{font-size:40px;color:var(--brown);line-height:20px;padding-top:18px}
.reviews p{font-size:14px;line-height:28px;margin-top:14px}
.stars{margin-top:18px}
.footer{height:491px;background:var(--footer);color:var(--white);position:relative}
.fcols{display:flex;padding:62px 35px 0}
.fcol h5{font-size:18px;letter-spacing:1px;text-transform:uppercase;margin-bottom:36px;font-weight:400}
.contact{width:303px;font-size:13px;line-height:22px}
.crow{display:flex;gap:14px;margin-bottom:14px;white-space:nowrap}
.crow svg{flex:none;margin-top:3px}
.subscribe{width:343px;font-size:13px;line-height:22px}
.subscribe .field{width:275px;height:34px;font-size:11px;padding:10px 14px;margin-top:20px}
.subscribe .btn{margin-top:18px;padding:9px 14px 6px;font-size:13px}
.links{font-size:13px}
.links ul{list-style:none;display:grid;grid-template-columns:112px 140px;grid-auto-flow:column;grid-template-rows:repeat(6,28px);white-space:nowrap}
.fbottom{position:absolute;left:0;right:0;top:323px;border-top:1px solid #3a302a;text-align:center;padding-top:44px}
.social{display:flex;justify-content:center;gap:8px}
.social span{width:36px;height:36px;border:2px solid var(--white);border-radius:50%}
.copy{font-size:13.5px;margin-top:23px}
</style>
</head>
<body>
<div class="backdrop" role="img" aria-label="Evening sky over pine forest with wooden deck boards on the sides"></div>
<div class="page">
  <header class="brand">
    <span class="brand-mark"></span>
    <span class="brand-name display">FERNHOLLOW LODGE RESORTS</span>
  </header>
  <nav class="nav">
    <a>Home</a><a>Cottage Info</a><a>House Info</a><a>Rates</a><a>How to find us</a><a>Info Request</a><a>Historical Info</a><a>Things to do</a><a>Contact us</a>
    <a class="phone">1-(888)-555-0142</a>
  </nav>
  <main class="main">
    <section class="hero" role="img" aria-label="Photo of a wooden lodge among tall pine trees at dusk">
      <svg class="arrow left" width="12" height="20" viewBox="0 0 12 20"><path d="M10 2 2 10l8 8" fill="none" stroke="#fff" stroke-width="3"/></svg>
      <svg class="arrow right" width="12" height="20" viewBox="0 0 12 20"><path d="M2 2l8 8-8 8" fill="none" stroke="#fff" stroke-width="3"/></svg>
      <h1 class="hero-title display">THE FERNHOLLOW<br>LODGE RESORTS</h1>
      <span class="btn display">Get More Info</span>
    </section>

    <section class="welcome">
      <h2 class="h2 display">Welcome to Fernhollow Lodges</h2>
      <p>Nestled in two acres of pine trees in Brindlemoor Vista, California, The Fernhollow Lodges is warm, clean and friendly. The Fernhollow Lodges consists of nineteen old Brindlemoor-style cottages, all with private bathrooms. Originally the sawmill and labor camp of the Halden Lumber Company, the property was converted to vacation cottages in 1925. Our cottages are all different–each with its own charm and modern conveniences. The Fernhollow Lodges is centrally located on the North Shore of Lake Brindlemoor, across the street from the lake–and just a stone’s throw away from a sandy beach and the water’s edge. We’re just minutes from great restaurants, shopping, North Shore casinos, and the worlds best skiing.</p>
      <h4 class="h4 display">All cottages include:</h4>
      <div class="amenities">
        <div class="amenity">
          <svg width="56" height="56" viewBox="0 0 56 56" fill="none" stroke="#7b4a1f" stroke-width="2"><rect x="10" y="8" width="36" height="16" rx="3"/><rect x="6" y="24" width="44" height="18"/><path d="M6 42v8M50 42v8M16 18h24"/></svg>
          Romantic Calder Iron Beds with comfortable Quillmoss mattresses with nice linens
        </div>
        <div class="amenity">
          <svg width="60" height="56" viewBox="0 0 60 56" fill="none" stroke="#7b4a1f" stroke-width="2"><rect x="4" y="12" width="52" height="32" rx="2"/><rect x="10" y="18" width="30" height="20"/><path d="M46 20h6M46 26h6M46 32h6M10 44v4M50 44v4"/></svg>
          Microwave Oven
        </div>
        <div class="amenity">
          <svg width="40" height="56" viewBox="0 0 40 56" fill="none" stroke="#7b4a1f" stroke-width="2"><rect x="8" y="4" width="24" height="46" rx="3"/><path d="M8 20h24M13 10v6M13 26v8"/></svg>
          Refrigerator
        </div>
        <div class="amenity">
          <svg width="56" height="56" viewBox="0 0 56 56" fill="none" stroke="#7b4a1f" stroke-width="2"><circle cx="28" cy="28" r="22"/><circle cx="28" cy="28" r="14"/><circle cx="28" cy="28" r="4"/></svg>
          Televisions with Lumacast and Video Tape/DVD Players
        </div>
        <div class="amenity">
          <svg width="50" height="56" viewBox="0 0 50 56" fill="none" stroke="#7b4a1f" stroke-width="2"><path d="M8 6h34v8H8zM12 14v36M6 50h38M20 24h18v14H20zM38 28h5v6h-5"/></svg>
          Coffee Maker
        </div>
        <div class="amenity">
          <svg width="56" height="56" viewBox="0 0 56 56" fill="none" stroke="#7b4a1f" stroke-width="2"><path d="M6 28h44M14 28l-6 22M42 28l6 22M20 28v22M36 28v22M28 6v14M22 14l6 6 6-6"/></svg>
          Porch with Calder Patio Furniture
        </div>
      </div>
    </section>

    <section class="newsletter" role="img" aria-label="Night photo of a lit cabin behind a stone driveway">
      <h2 class="h2 display">Join our Newsletter</h2>
      <p>We respect your privacy. We will not share your email address<br>with any third party vendors.</p>
      <div class="signup"><span class="field">Enter your E - mail</span><span class="btn display">Subscribe</span></div>
    </section>

    <section class="features">
      <article class="feature">
        <h3 class="h3 display">Brindlemoor Vista Lodge</h3>
        <div class="photo lodge" role="img" aria-label="Photo of a dark lodge among pines with a garden path"></div>
        <p>The Brindlemoor Vista Lodge &amp; Cabins are located one mile west of the Fernhollow Lodges. Originally the Marlowe's Resort built between 1943 and 1947 by Edwin Harlan Marlowe, this property has had many names and owners over the years.</p>
        <span class="outline-btn display">Read More <svg width="14" height="10" viewBox="0 0 14 10"><path d="M0 5h12M8 1l4 4-4 4" fill="none" stroke="#2a2420" stroke-width="1.5"/></svg></span>
      </article>
      <article class="feature">
        <h3 class="h3 display">Fernhollow Lodges</h3>
        <div class="photo cottage" role="img" aria-label="Photo of a wooden cottage with flags and flowerbeds under pines"></div>
        <p>Nestled in two acres of pine trees in Brindlemoor Vista, California, The Fernhollow Lodges is warm, clean and friendly. The Fernhollow Lodges consists of nineteen old Brindlemoor-style cottages, all with private bathrooms. Originally the sawmill and labor</p>
        <span class="outline-btn display">Read More <svg width="14" height="10" viewBox="0 0 14 10"><path d="M0 5h12M8 1l4 4-4 4" fill="none" stroke="#2a2420" stroke-width="1.5"/></svg></span>
      </article>
    </section>

    <section class="reviews">
      <h2 class="h2 display">Customers Reviews</h2>
      <div class="reviewer display"><span class="quote">“</span>Blandit Lectus<span class="quote">”</span></div>
      <p>Sed ut perspiciatis unde omnis iste natus error sit voluptatem accusantium doloremque laudantium, totam rem aperiam, eaque ipsa quae ab illo inventore veritatis et quasi architecto beatae vitae dicta sunt explicabo. Nemo enim ipsam voluptatem quia voluptas sit aspernatur aut odit aut fugit Sed ut perspiciatis unde omnis</p>
      <svg class="stars" width="112" height="20" viewBox="0 0 112 20" fill="none" stroke="#2a2420" stroke-width="1.3">
        <path id="star" d="M10 1l2.6 6 6.4.5-4.9 4.2 1.5 6.3L10 14.6 4.4 18l1.5-6.3L1 7.5l6.4-.5z"/>
        <use href="#star" x="23"/><use href="#star" x="46"/><use href="#star" x="69"/><use href="#star" x="92"/>
      </svg>
    </section>
  </main>

  <footer class="footer">
    <div class="fcols">
      <div class="fcol contact">
        <h5 class="display">Contact Us</h5>
        <div class="crow"><svg width="14" height="18" viewBox="0 0 14 18" fill="none" stroke="#fff" stroke-width="1.4"><path d="M7 17s6-6.5 6-10.5A6 6 0 0 0 1 6.5C1 10.5 7 17 7 17z"/><circle cx="7" cy="6.5" r="2"/></svg><span>Fernhollow Lodges,<br>212 Cedar Shore Road,<br>P.O. Box 42, Brindlemoor Vista,<br>CA 90210</span></div>
        <div class="crow"><svg width="16" height="16" viewBox="0 0 16 16" fill="none" stroke="#fff" stroke-width="1.4"><path d="M4 1l3 4-2 2c1 2 2 3 4 4l2-2 4 3-2 3C7 15 1 9 1 3z"/></svg><span>Phone :&nbsp; 1-(888)-555-0142</span></div>
        <div class="crow"><svg width="16" height="12" viewBox="0 0 16 12" fill="none" stroke="#fff" stroke-width="1.4"><rect x="1" y="1" width="14" height="10"/><path d="M1 1l7 6 7-6"/></svg><span>Email : info@fernhollowlodges-example.com</span></div>
      </div>
      <div class="fcol subscribe">
        <h5 class="display">Sign up to receive Email</h5>
        <p>Excepteur sint occaecat cupidatat non proident,<br>sunt in culpa qui Nemo</p>
        <div class="field">Enter Email</div>
        <span class="btn display">Subscribe</span>
      </div>
      <div class="fcol links">
        <h5 class="display">Quick Links</h5>
        <ul><li>Home</li><li>Cottage Info</li><li>House Info</li><li>Rates</li><li>How to find us</li><li>Info Request</li><li>Historical Info</li><li>Things to do</li><li>Contact Us</li><li>Brindlemoor Vista Lodge</li></ul>
      </div>
    </div>
    <div class="fbottom">
      <div class="social"><span></span><span></span><span></span><span></span></div>
      <p class="copy">Copyright © The Fernhollow Lodges. 2019. All rights reserved.</p>
    </div>
  </footer>
</div>
</body>
</html>
```